Vantor Ridged Concrete & Grinding
I'm looking for a business card and logo design for my
new Polished Concrete & Grinding business,
If you were to look up Vantor in the dictionary it would
say, first in importance, order, or position; leading.
Polished Concrete floors are a niche market, that are being used currently in Shopping centres, office spaces and by most high end architects, builders and designers.
i need my business card & logo to stand out from my
competitors, i need my design + logo to reflect this it
needs to be simple, professional, eye catching, easy
to read and scream quality. The logo will need to be
suitable for a whole range of applications including,
uniforms, letter heads, stickers, and eventually
incorporating in vehicle vinyl wrapping.
Target Market(s)
Builders, architects, Interior designers & home owners
Contact Information for Business Card
Front side:
- Vantor Ridged Concrete & Grinding.
- Logo
Rear side:
- Neil Varbusk
- 0491587302
- info@vantorrcg.com.au
- commercial - domestic - industrial
- (later down the line website & space for
social media links
www.vantorridgedconcrete.com.au)
Colors
Designer to choose colors to be used in the design.
Look and feel

```html
<!DOCTYPE html>
<html lang="en">
<head>
<meta charset="utf-8">
<title>Vantor Ridged Concrete &amp; Grinding — Business Card</title>
<link rel="stylesheet" href="https://fonts.googleapis.com/css2?family=Roboto:wght@400;500&display=swap">
<style>
  :root {
    --backdrop: #b4b4b4;
    --brand-blue: #22a7df;
    --card-white: #ffffff;
    --ink: #1d1d1d;
    --muted: #333333;
  }
  * { box-sizing: border-box; margin: 0; padding: 0; }
  html, body { width: 1200px; height: 930px; overflow: hidden; }
  body {
    background: var(--backdrop);
    font-family: "Roboto", Arial, sans-serif;
    position: relative;
  }
  .card {
    position: absolute;
    width: 560px;
    height: 320px;
    border-radius: 22px;
    box-shadow: 0 6px 14px rgba(0,0,0,0.25);
  }
  .card--front { left: 90px; top: 110px; background: var(--brand-blue); }
  .card--back { left: 550px; top: 500px; background: var(--card-white); }

  .wordmark {
    display: flex;
    align-items: center;
    gap: 12px;
    font-weight: 500;
    text-transform: uppercase;
    letter-spacing: 0.04em;
    line-height: 1.15;
  }
  .wordmark__dot {
    width: 18px; height: 18px; border-radius: 50%; flex: none;
  }
  .card--front .wordmark {
    position: absolute; left: 0; right: 0; top: 100px;
    justify-content: center; color: var(--card-white);
  }
  .card--front .wordmark__dot { background: var(--card-white); }
  .wordmark__name { font-size: 30px; }
  .wordmark__sub { font-size: 16px; display: block; }

  .services {
    position: absolute; left: 0; right: 0; bottom: 34px;
    text-align: center; color: var(--card-white);
    font-size: 17px; letter-spacing: 0.03em;
  }

  .card--back .wordmark {
    position: absolute; left: 36px; top: 128px;
    color: var(--brand-blue);
  }
  .card--back .wordmark__dot { background: var(--brand-blue); }
  .card--back .wordmark__name { font-size: 23px; }
  .card--back .wordmark__sub { font-size: 12.5px; }

  .divider {
    position: absolute; left: 272px; top: 78px;
    width: 2px; height: 150px; background: var(--brand-blue);
  }
  .contact { position: absolute; left: 298px; top: 74px; }
  .contact__name {
    color: var(--brand-blue); font-size: 30px; font-weight: 400;
    letter-spacing: 0.06em; text-transform: uppercase;
  }
  .contact__role { color: var(--ink); font-size: 15px; margin: 2px 0 18px 4px; }
  .contact__list { list-style: none; margin-left: 4px; }
  .contact__item {
    display: flex; align-items: center; gap: 9px;
    color: var(--muted); font-size: 15px; margin-bottom: 7px;
  }
  .contact__icon { width: 11px; height: 11px; flex: none; }
</style>
</head>
<body>
  <section class="card card--front" aria-label="Card front">
    <div class="wordmark">
      <span class="wordmark__dot"></span>
      <span><span class="wordmark__name">Vantor Ridged</span><span class="wordmark__sub">Concrete &amp; Grinding.</span></span>
    </div>
    <p class="services">COMMERCIAL - DOMESTIC - INDUSTRIAL</p>
  </section>

  <section class="card card--back" aria-label="Card back">
    <div class="wordmark">
      <span class="wordmark__dot"></span>
      <span><span class="wordmark__name">Vantor Ridged</span><span class="wordmark__sub">Concrete &amp; Grinding.</span></span>
    </div>
    <div class="divider"></div>
    <div class="contact">
      <h1 class="contact__name">Neil Varbusk</h1>
      <p class="contact__role">Director</p>
      <ul class="contact__list">
        <li class="contact__item">
          <svg class="contact__icon" viewBox="0 0 12 12" aria-hidden="true"><path d="M2.5 1 L4.5 1 L5.2 3.5 L4 4.6 Q5 7 7.4 8 L8.5 6.8 L11 7.5 L11 9.5 Q10.5 11 9 11 Q1 10 1 3 Q1 1.5 2.5 1Z" fill="#22a7df"/></svg>
          0491587302
        </li>
        <li class="contact__item">
          <svg class="contact__icon" viewBox="0 0 12 12" aria-hidden="true"><rect x="1" y="2.5" width="10" height="7" fill="none" stroke="#22a7df" stroke-width="1.3"/><path d="M1 2.5 L6 6.5 L11 2.5" fill="none" stroke="#22a7df" stroke-width="1.3"/></svg>
          info@vantorrcg.com.au
        </li>
        <li class="contact__item">
          <svg class="contact__icon" viewBox="0 0 12 12" aria-hidden="true"><circle cx="6" cy="6" r="5" fill="none" stroke="#22a7df" stroke-width="1.2"/><ellipse cx="6" cy="6" rx="2.2" ry="5" fill="none" stroke="#22a7df" stroke-width="1"/><path d="M1 6 H11" stroke="#22a7df" stroke-width="1"/></svg>
          www.vantorridgedconcrete.com.au
        </li>
      </ul>
    </div>
  </section>
</body>
</html>
```